Eyecatching Carpentry Business card

I need a business card designed for myself, my company name is Tom Hadfield Carpentry.
I am based on the south coast of England and I do all aspects of carpentry, including;
skirting
Architraves
kitchens
roof construction
flooring
doors
loft conversions
decking
windows
I currently have no company logo or letter head so I leave all design ideas to designers.
All I ask is that it looks professional and modern.
A logo may be incorporated as well.
My contact details should be on the back, telephone and email.

```html
<!DOCTYPE html>
<html lang="en">
<head>
<meta charset="utf-8">
<title>Tom Hadfield Carpentry – Business Card</title>
<link rel="stylesheet" href="https://fonts.googleapis.com/css2?family=Cinzel:wght@400&family=Open+Sans:wght@400;600;700&display=swap">
<style>
  :root {
    --page-bg: #e9e6e2;
    --card-bg: #eecfb5;
    --ink: #1c1a18;
    --ink-soft: #2e2a26;
    --rule: #8a7d72;
    --mark: #9a6438;
    --card-shadow: rgba(60, 40, 20, 0.18);
  }
  html, body {
    margin: 0;
    width: 1200px;
    height: 918px;
    overflow: hidden;
    background: var(--page-bg);
  }
  .sheet {
    width: 1200px;
    height: 918px;
    display: flex;
    align-items: center;
    justify-content: center;
    gap: 60px;
  }
  .card {
    position: relative;
    width: 520px;
    height: 297px;
    background: var(--card-bg);
    box-shadow: 0 6px 18px var(--card-shadow);
    box-sizing: border-box;
  }
  /* Front */
  .card--front .brand-mark {
    position: absolute;
    left: 50%;
    top: 48px;
    width: 116px;
    height: 116px;
    margin-left: -58px;
  }
  .card--front .brand-name {
    position: absolute;
    left: 0;
    right: 0;
    top: 184px;
    margin: 0;
    text-align: center;
    font-family: "Cinzel", serif;
    font-weight: 400;
    font-size: 25px;
    letter-spacing: 2px;
    color: var(--ink);
  }
  .card--front .brand-rule {
    position: absolute;
    left: 105px;
    right: 105px;
    top: 224px;
    height: 0;
    border-top: 1.5px solid var(--rule);
  }
  /* Back */
  .card--back .contact {
    position: absolute;
    left: 46px;
    top: 38px;
    font-family: "Open Sans", sans-serif;
    color: var(--ink-soft);
  }
  .contact__name {
    margin: 0;
    font-size: 20px;
    font-weight: 700;
    line-height: 1.05;
    color: var(--ink);
  }
  .contact__title {
    margin: 0 0 18px;
    font-size: 12px;
    font-weight: 600;
  }
  .contact__address,
  .contact__phone,
  .contact__email {
    margin: 0 0 16px;
    font-size: 15px;
    font-weight: 600;
    line-height: 1.2;
    font-style: normal;
  }
</style>
</head>
<body>
  <main class="sheet">
    <section class="card card--back" aria-label="Card back">
      <div class="contact">
        <p class="contact__name">Your Name</p>
        <p class="contact__title">Your Title</p>
        <address class="contact__address">Sample Address<br>Sample Street</address>
        <p class="contact__phone">123456789</p>
        <p class="contact__email">sample@sample.com</p>
      </div>
    </section>

    <section class="card card--front" aria-label="Card front">
      <svg class="brand-mark" viewBox="0 0 116 116" aria-hidden="true">
        <circle cx="58" cy="58" r="58" fill="var(--mark)"/>
      </svg>
      <h1 class="brand-name">Tom Hadfield Carpentry</h1>
      <div class="brand-rule"></div>
    </section>
  </main>
</body>
</html>
```